Harbor Keyvault Password Manager WebApp Design

Harbor Keyvault is seeking an expert UI designer to provide a fresh and modern visual appeal for our product. Our inspiration comes from two major tools that have successfully managed to balance functionality and design aesthetics - Nimbus Folio and LockTrellis. We want our application to exude a similar trustworthiness and modernity, through a clean, intuitive and responsive design.
We have established preliminary mockups and would like the designer to work within these parameters while enhancing the overall user experience. The primary tasks will involve innovative and improved designs of the login screen and the password screen, both being crucial touchpoints for our users. The login screen also serves a crucial role in demonstrating how our system works.
Key Elements:
Logo Integration: We are providing the logo for Harbor Keyvault. The design should align with the logo, both in terms of colors and overall aesthetic, to ensure a cohesive brand identity.
Color Palette: The UI design should adhere to the color palette derived from the logo to maintain brand consistency. The design should effectively utilize these colors to highlight important elements and improve user engagement.
Trustworthy and Modern Design: The UI should be professional and trustworthy. It should mirror the look and feel of Nimbus Folio's simplicity and LockTrellis's solid security design, which inspires user confidence.
Adherence to Mockup Boundaries: The existing mockups serve as a guideline for the layout and placement of elements. The design should respect these boundaries while bringing innovation and visual appeal.
Improved Login Screen: The login screen is a key part of the user's journey and should be designed with utmost care. It should be intuitive, easy-to-use, visually engaging, and educative, showcasing how the system operates and encouraging users to sign in with confidence.
Enhanced Password Screen: The password screen, another key user touchpoint, needs improvement. The different types of passwords should be made more visible and intuitive, easing user interaction and enhancing the overall experience.
Prospective designers are encouraged to test our current version available for free at app.harborkeyvault.example to understand the product better and contribute to meaningful design enhancements.
The goal of this project is to provide a visually compelling and user-friendly interface for Harbor Keyvault that inspires user trust, while adhering to the branding elements, including color scheme and logo design. The ideal designer will have a proven track record of creating compelling UI designs that enhance user experience and engagement.
We preferred the design to be in Figma.
Please provide the 3 design so we can evaluate if we like to choice you:
1. Login Page.
2. Passwords View design
3. Single Passwod Page
We need all the pages to be design that are provided as screenshots.
Target Market(s)
Companies
Industry/Entity Type
Security,
Number of Pages Required
5+ page
Font styles to use
Look and feel
Each slider illustrates characteristics of the customer's brand and the style your logo design should communicate.

```html
<!DOCTYPE html>
<html lang="en">
<head>
<meta charset="utf-8">
<title>Harbor Keyvault — Login and Vault</title>
<link href="https://fonts.googleapis.com/css2?family=Inter:wght@300;400;500;600;700&display=swap" rel="stylesheet">
<style>
:root{
  --bg:#263036;
  --blue:#2f8cf0;
  --blue-deep:#2a86ea;
  --blue-text:#3b8fe8;
  --green:#1fc46a;
  --green-soft:#e9fbf0;
  --ink:#1d2330;
  --muted:#8fa3b8;
  --line:#e3ebf3;
  --panel:#ffffff;
  --peach:#fff0ea;
  --search:#e2f4fc;
  --forgot:#179a4b;
}
*{box-sizing:border-box;margin:0;padding:0}
html,body{width:1200px;height:1200px;overflow:hidden;background:var(--bg)}
body{font-family:"Inter",sans-serif;color:var(--ink)}
.stage{position:absolute;left:0;top:0;width:1900px;height:1900px;transform:scale(.631579);transform-origin:0 0}
.abs{position:absolute}

/* ---------- Login screen ---------- */
.login{left:266px;top:150px;width:1366px;height:768px;background:#fff;overflow:hidden}
.login-hero{left:0;top:0;width:757px;height:768px;background:radial-gradient(circle at 50% 55%,#74b8fb 0%,#3d96f2 45%,#2f8cf0 100%)}
.hero-art{left:154px;top:90px;width:460px;height:450px;border-radius:40px;
  background:radial-gradient(ellipse at 50% 45%,#f1f5ff 0%,#cfd9fb 35%,#8fb6f6 60%,rgba(80,160,245,0) 75%)}
.hero-caption{left:0;top:580px;width:757px;text-align:center;color:#fff;font-weight:300;font-size:16px;line-height:22px}
.hero-dots{left:353px;top:668px;display:flex;gap:13px}
.hero-dots span{width:8px;height:8px;background:rgba(255,255,255,.45)}
.hero-dots span:first-child{background:#fff}
.how{left:41px;top:713px;display:flex;align-items:center;gap:12px;color:rgba(255,255,255,.7);font-size:10px}
.how i{width:19px;height:19px;background:rgba(255,255,255,.35);color:#fff;font-style:normal;font-weight:600;font-size:13px;display:flex;align-items:center;justify-content:center;border-radius:2px}

.login-form-area{left:757px;top:0;width:609px;height:768px;
  background:radial-gradient(circle at 15% 62%,rgba(120,220,235,.45) 0%,rgba(255,255,255,0) 35%),
             radial-gradient(circle at 85% 55%,rgba(245,200,205,.5) 0%,rgba(255,255,255,0) 35%),#fafcfd}
.brand-top{left:192px;top:42px;display:flex;align-items:center;gap:22px}
.brand-mark{width:58px;height:58px;background:#fff;border-radius:6px;box-shadow:0 2px 10px rgba(0,0,0,.05)}
.brand-top .brand-name{font-size:24px;font-weight:500;color:var(--blue-text)}
.welcome{left:0;top:218px;width:609px;text-align:center;font-size:36px;font-weight:600;color:var(--blue-text)}
.field{left:146px;width:332px;height:47px;background:#fff;border-radius:6px;display:flex;align-items:center;padding:0 14px;gap:14px;font-size:13px;color:#9cc2e0;box-shadow:0 2px 10px rgba(80,120,160,.05)}
.field .forgot{margin-left:auto;color:var(--forgot);font-size:14px}
.btn-login{left:146px;top:450px;width:332px;height:47px;background:var(--blue);border-radius:8px;color:#fff;font-size:14px;font-weight:600;display:flex;align-items:center;justify-content:center;box-shadow:0 6px 14px rgba(47,140,240,.3)}
.or{left:0;top:558px;width:609px;text-align:center;font-size:14px;color:var(--ink)}
.btn-provider{left:270px;top:593px;width:84px;height:45px;background:#fff;border-radius:6px;display:flex;align-items:center;justify-content:center;font-size:14px;font-weight:500;color:var(--ink);box-shadow:0 2px 10px rgba(0,0,0,.06)}
.legal{left:0;width:609px;text-align:center;font-size:9.5px;color:var(--ink)}
.legal a{color:var(--blue);text-decoration:none}

/* ---------- Vault screen ---------- */
.vault{left:266px;top:981px;width:1366px;height:768px;background:#f6fafd;overflow:hidden}
.side-brand{left:26px;top:30px;display:flex;align-items:center;gap:14px}
.side-brand .brand-mark{width:40px;height:40px}
.side-brand .brand-name{font-size:17px;font-weight:500;color:var(--blue-text)}
.nav-item{left:13px;width:204px;height:48px;display:flex;align-items:center;gap:18px;padding-left:14px;font-size:14px;color:var(--ink)}
.nav-item svg{width:22px;height:22px}
.nav-item.active{background:var(--blue);border-radius:6px;color:#fff;font-weight:600}
.side-divider{left:17px;width:200px;height:2px;background:var(--line)}
.side-heading{left:31px;font-size:14px;font-weight:600}
.settings{left:28px;top:710px}
.avatar{left:88px;top:702px;width:41px;height:41px;border-radius:50%;background:radial-gradient(circle at 50% 40%,#c9866a 0%,#6a3a30 55%,#2b6f8a 100%)}

.search{left:295px;top:30px;width:687px;height:38px;background:var(--search);border-radius:8px;padding-left:34px;display:flex;align-items:center;font-size:14px;color:#5aa8d8}
.btn-add{left:1022px;top:24px;width:129px;height:50px;background:var(--green);border-radius:6px;display:flex;align-items:center;justify-content:center;gap:14px;color:#fff;font-size:20px;font-weight:500}
.top-icon{top:38px}

.main{left:265px;top:94px;width:1079px;height:648px;background:#fff;border-radius:10px;box-shadow:0 4px 20px rgba(60,120,180,.06)}
.recent{left:30px;top:39px;width:1024px;height:208px;border:1.5px solid #a9d4f4;border-radius:10px}
.section-title{font-size:14px;font-weight:600;color:var(--ink)}
.tile{top:72px;height:98px;border-radius:8px;padding:26px 12px 0;white-space:nowrap;overflow:hidden}
.tile .t-head{display:flex;align-items:center;gap:12px;font-size:14px;font-weight:600}
.tile .t-sub{margin-top:14px;font-size:12px}
.tile-fade{left:960px;top:70px;width:30px;height:102px;background:linear-gradient(90deg,rgba(255,255,255,0),#fff)}

.drive{left:30px;top:270px;width:718px;height:347px;background:var(--peach);border-radius:10px}
.row{left:30px;width:646px;height:45px;background:#fff;border-radius:6px;box-shadow:0 2px 8px rgba(240,150,110,.08)}
.row .check{position:absolute;left:18px;top:16px;width:13px;height:13px;border:1.5px solid #f5cf6a;border-radius:2px}
.row .check.on{background:#f9d96e;box-shadow:inset 0 0 0 2px #fff}
.row .folder{position:absolute;left:50px;top:13px}
.row .name{position:absolute;left:92px;top:13px;font-size:14px}
.row .date{position:absolute;left:473px;top:14px;font-size:14px;color:#3a4250}
.row .dots{position:absolute;left:618px;top:14px}
.row.current .name{font-weight:600}

.details{left:772px;top:270px;width:281px;height:347px;background:var(--green-soft);border-radius:10px}
.details .label{position:absolute;left:25px;font-size:10px;font-weight:500;color:var(--ink)}
.details .value{position:absolute;left:25px;font-size:14px;color:#5a6472}
.details .scroll{position:absolute;left:268px;top:34px;width:4px;height:210px;background:#8fe0b0;border-radius:2px}
</style>
</head>
<body>
<div class="stage">

  <!-- Login -->
  <section class="abs login">
    <div class="abs login-hero">
      <div class="abs hero-art" role="img" aria-label="Illustration: laptop with fingerprint scan, credit card, password field and padlock, a person holding a large key"></div>
      <p class="abs hero-caption">Only you from your browser can connect to your<br>Nimbus Folio. We do not have any access to it</p>
      <div class="abs hero-dots"><span></span><span></span><span></span></div>
      <div class="abs how"><i>?</i>How it Works</div>
    </div>

    <div class="abs login-form-area">
      <div class="abs brand-top"><span class="brand-mark"></span><span class="brand-name">Harbor Keyvault</span></div>
      <h1 class="abs welcome">Welcome Back</h1>

      <div class="abs field" style="top:320px">
        <svg width="18" height="14" viewBox="0 0 18 14" fill="none" stroke="#8fc0ea" stroke-width="1.4"><rect x="1" y="1" width="16" height="12" rx="1.5"/><path d="M1.5 2l7.5 6 7.5-6"/></svg>
        <span>Enter your email</span>
      </div>
      <div class="abs field" style="top:385px">
        <svg width="16" height="18" viewBox="0 0 16 18" fill="none" stroke="#8fc0ea" stroke-width="1.4"><rect x="2" y="8" width="12" height="9" rx="1.5"/><path d="M4.5 8V5a3.5 3.5 0 017 0v3"/><circle cx="8" cy="12.5" r="1"/></svg>
        <span>Enter password</span>
        <span class="forgot">Forgot Password?</span>
      </div>
      <div class="abs btn-login">Login</div>

      <p class="abs or">Or continue with</p>
      <div class="abs btn-provider">Nimbus</div>

      <p class="abs legal" style="top:690px">By clicking Sign In with Nimbus, you agree with our <a>Terms of Use</a></p>
      <p class="abs legal" style="top:710px">Learn what data we collect and how we handle it in our <a>Privacy Policy</a></p>
    </div>
  </section>

  <!-- Vault -->
  <section class="abs vault">
    <div class="abs side-brand"><span class="brand-mark"></span><span class="brand-name">Harbor Keyvault</span></div>

    <div class="abs nav-item active" style="top:95px">
      <svg viewBox="0 0 22 22" fill="none"><rect x="2" y="4" width="18" height="14" rx="2" fill="#fff" opacity=".35"/><circle cx="12" cy="11" r="4" fill="#fff"/><rect x="4" y="7" width="2" height="8" fill="#fff"/></svg>Vault</div>
    <div class="abs nav-item" style="top:148px">
      <svg viewBox="0 0 22 22"><circle cx="7" cy="8" r="3" fill="#bcdaf5"/><circle cx="15" cy="8" r="3" fill="#bcdaf5"/><circle cx="11" cy="7" r="3" fill="#8cc2f0"/><path d="M2 17c0-4 18-4 18 0v1H2z" fill="#a9d0f4"/></svg>Teams</div>
    <div class="abs nav-item" style="top:200px">
      <svg viewBox="0 0 22 22" fill="none"><path d="M7 10V7a4 4 0 018 0v3" stroke="#a9d0f4" stroke-width="1.8"/><rect x="4" y="10" width="14" height="10" rx="2" fill="#cfe5f8"/><circle cx="8" cy="15" r="1" fill="#7cb8ec"/><circle cx="11" cy="15" r="1" fill="#7cb8ec"/><circle cx="14" cy="15" r="1" fill="#7cb8ec"/></svg>Password Generator</div>
    <div class="abs nav-item" style="top:252px">
      <svg viewBox="0 0 22 22" fill="none"><rect x="2" y="4" width="14" height="14" rx="2" fill="#cfe5f8"/><circle cx="13" cy="12" r="4" stroke="#6fb2ec" stroke-width="1.8"/><path d="M16 15l4 4" stroke="#6fb2ec" stroke-width="1.8"/><path d="M5 8h5M5 12h3" stroke="#6fb2ec" stroke-width="1.4"/></svg>Overview</div>

    <div class="abs side-divider" style="top:311px"></div>
    <div class="abs side-heading" style="top:327px">Category</div>

    <div class="abs nav-item" style="top:366px">
      <svg viewBox="0 0 22 22"><path d="M3 10l8-6 8 6v9H3z" fill="#cfe5f8"/><rect x="9" y="13" width="4" height="6" fill="#8cc2f0"/></svg>General</div>
    <div class="abs nav-item" style="top:418px">
      <svg viewBox="0 0 22 22"><circle cx="11" cy="6" r="3" fill="#8cc2f0"/><circle cx="5" cy="15" r="2.5" fill="#bcdaf5"/><circle cx="17" cy="15" r="2.5" fill="#bcdaf5"/><path d="M1 21c0-3 8-3 8 0zM13 21c0-3 8-3 8 0z" fill="#a9d0f4"/></svg>Social Media</div>
    <div class="abs nav-item" style="top:470px">
      <svg viewBox="0 0 22 22"><rect x="3" y="5" width="16" height="13" rx="2" fill="#cfe5f8"/><circle cx="9" cy="10" r="2" fill="#6fb2ec"/><circle cx="14" cy="14" r="2" fill="#8cc2f0"/></svg>Travel</div>
    <div class="abs nav-item" style="top:525px">
      <svg viewBox="0 0 22 22"><path d="M2 6h7l2 2h9v11H2z" fill="#cfe5f8"/><circle cx="11" cy="12" r="2" fill="#6fb2ec"/><path d="M7 17c0-3 8-3 8 0z" fill="#6fb2ec"/></svg>Shared With Me</div>

    <div class="abs side-divider" style="top:593px"></div>
    <div class="abs nav-item" style="top:610px">
      <svg viewBox="0 0 22 22"><rect x="5" y="7" width="12" height="13" rx="1.5" fill="#cfe5f8"/><rect x="3" y="4" width="16" height="3" rx="1" fill="#a9d0f4"/></svg>Trash</div>

    <svg class="abs settings" width="22" height="22" viewBox="0 0 22 22"><circle cx="11" cy="11" r="7" fill="none" stroke="#8cc2f0" stroke-width="4" stroke-dasharray="3.5 2"/><circle cx="11" cy="11" r="5" fill="#8cc2f0"/><circle cx="11" cy="11" r="2" fill="#fff"/></svg>
    <div class="abs avatar" role="img" aria-label="User profile photo"></div>

    <div class="abs search">Search</div>
    <div class="abs btn-add">
      <svg width="26" height="26" viewBox="0 0 26 26" fill="none" stroke="#fff" stroke-width="2"><rect x="3" y="6" width="16" height="17" rx="1.5"/><path d="M7 12h8M7 16h8M7 20h5M21 2v8M17 6h8"/></svg>Add</div>
    <svg class="abs top-icon" style="left:1182px" width="20" height="20" viewBox="0 0 20 20"><path d="M2 2h16v12H6l-4 4z" fill="#7edaa5"/><path d="M5 6h10M5 9h10M5 12h6" stroke="#fff" stroke-width="1.4"/></svg>
    <svg class="abs top-icon" style="left:1232px" width="18" height="20" viewBox="0 0 18 20"><path d="M9 2c4 0 6 3 6 6v5l2 2H1l2-2V8c0-3 2-6 6-6z" fill="#7edaa5"/><circle cx="9" cy="18" r="2" fill="#7edaa5"/></svg>
    <svg class="abs top-icon" style="left:1282px" width="16" height="20" viewBox="0 0 16 20"><path d="M1 1h14v18l-7-5-7 5z" fill="#7edaa5"/></svg>

    <div class="abs main">
      <div class="abs recent">
        <div class="abs section-title" style="left:30px;top:21px">Last Used</div>

        <div class="abs tile" style="left:30px;width:114px;background:#fdc9c1">
          <div class="t-head" style="color:#ec4a3a"><svg width="22" height="18" viewBox="0 0 22 18"><path d="M1 2h8l2 2h10v13H1z" fill="#ec4a3a"/></svg>General</div>
          <div class="t-sub" style="color:#f06a5c">Manage Access</div></div>
        <div class="abs tile" style="left:163px;width:113px;background:#e6eefc">
          <div class="t-head" style="color:#3a78e6"><svg width="22" height="18" viewBox="0 0 22 18"><path d="M1 2h8l2 2h10v13H1z" fill="#3a78e6"/></svg>General</div>
          <div class="t-sub" style="color:#6a94d8">Manage Access</div></div>
        <div class="abs tile" style="left:296px;width:113px;background:#fff0e4">
          <div class="t-head" style="color:#f5932c"><svg width="22" height="18" viewBox="0 0 22 18"><path d="M1 2h8l2 2h10v13H1z" fill="#f7a04a"/></svg>General</div>
          <div class="t-sub" style="color:#f7a760">Manage Access</div></div>
        <div class="abs tile" style="left:428px;width:112px;background:#e0f6fc">
          <div class="t-head" style="color:#3ac0e6;font-weight:400"><svg width="22" height="18" viewBox="0 0 22 18"><rect x="1" y="4" width="20" height="13" rx="1.5" fill="#3ac0e6"/><path d="M7 4V1h8v3" fill="none" stroke="#3ac0e6" stroke-width="2"/></svg>Work</div>
          <div class="t-sub" style="color:#5ccbe9">Manage Access</div></div>
        <div class="abs tile" style="left:560px;width:163px;background:#dcf8e6">
          <div class="t-head" style="color:#1fb866;font-weight:400"><svg width="22" height="18" viewBox="0 0 22 18"><path d="M1 2h8l2 2h10v13H1z" fill="#1fb866"/><circle cx="13" cy="9" r="2" fill="#dcf8e6"/><path d="M9 14c0-3 8-3 8 0z" fill="#dcf8e6"/></svg>Shared with me</div>
          <div class="t-sub" style="color:#3cc77c">Manage Access</div></div>
        <div class="abs tile" style="left:743px;width:112px;background:#e6eefc">
          <div class="t-head" style="color:#3a78e6;font-weight:400"><svg width="22" height="20" viewBox="0 0 22 20" fill="none" stroke="#3a78e6" stroke-width="1.8"><rect x="1" y="5" width="20" height="14" rx="2"/><path d="M7 5V1h8v4M1 11h20"/></svg>Travel</div>
          <div class="t-sub" style="color:#6a94d8">Manage Access</div></div>
        <div class="abs tile" style="left:874px;width:110px;background:#fff0e4">
          <div class="t-head" style="color:#f5932c;font-weight:400"><svg width="22" height="16" viewBox="0 0 22 16"><rect x="1" y="1" width="20" height="14" rx="1.5" fill="#f7a04a"/><path d="M2 2l9 7 9-7" fill="none" stroke="#fff" stroke-width="1.6"/></svg>Mail</div>
          <div class="t-sub" style="color:#f7a760">Manage Access</div></div>
        <div class="abs tile-fade"></div>
        <svg class="abs" style="left:992px;top:110px" width="14" height="22" viewBox="0 0 14 22" fill="none" stroke="#3ab0ef" stroke-width="2.4"><path d="M3 2l8 9-8 9"/></svg>
      </div>

      <div class="abs drive">
        <div class="abs section-title" style="left:30px;top:16px">My Drive</div>
        <div class="abs row current" style="top:50px"><span class="check on"></span>
          <svg class="folder" width="22" height="18" viewBox="0 0 22 18" fill="none" stroke="#f5c542" stroke-width="1.6"><path d="M1 2h7l2 2h11v13H1z"/><path d="M1 6h20"/></svg>
          <span class="name" style="left:92px">Social Media</span><span class="date">03 June 2023</span>
          <svg class="dots" width="6" height="18" viewBox="0 0 6 18" fill="#1d2330"><circle cx="3" cy="3" r="1.8"/><circle cx="3" cy="9" r="1.8"/><circle cx="3" cy="15" r="1.8"/></svg></div>
        <div class="abs row" style="top:108px"><span class="check"></span>
          <svg class="folder" width="22" height="18" viewBox="0 0 22 18" fill="none" stroke="#f5c542" stroke-width="1.6"><path d="M1 2h7l2 2h11v13H1z"/><path d="M1 6h20"/></svg>
          <span class="name" style="left:95px">Work</span><span class="date">03 June 2023</span>
          <svg class="dots" width="6" height="18" viewBox="0 0 6 18" fill="#1d2330"><circle cx="3" cy="3" r="1.8"/><circle cx="3" cy="9" r="1.8"/><circle cx="3" cy="15" r="1.8"/></svg></div>
        <div class="abs row" style="top:166px"><span class="check"></span>
          <svg class="folder" width="22" height="18" viewBox="0 0 22 18" fill="none" stroke="#f5c542" stroke-width="1.6"><path d="M1 2h7l2 2h11v13H1z"/><path d="M1 6h20"/></svg>
          <span class="name" style="left:94px">Banking</span><span class="date">03 June 2023</span>
          <svg class="dots" width="6" height="18" viewBox="0 0 6 18" fill="#1d2330"><circle cx="3" cy="3" r="1.8"/><circle cx="3" cy="9" r="1.8"/><circle cx="3" cy="15" r="1.8"/></svg></div>
        <div class="abs row" style="top:224px"><span class="check"></span>
          <svg class="folder" width="22" height="18" viewBox="0 0 22 18" fill="none" stroke="#f5c542" stroke-width="1.6"><path d="M1 2h7l2 2h11v13H1z"/><path d="M1 6h20"/></svg>
          <span class="name">Authentication</span><span class="date">03 June 2023</span>
          <svg class="dots" width="6" height="18" viewBox="0 0 6 18" fill="#1d2330"><circle cx="3" cy="3" r="1.8"/><circle cx="3" cy="9" r="1.8"/><circle cx="3" cy="15" r="1.8"/></svg></div>
        <div class="abs row" style="top:282px"><span class="check"></span>
          <svg class="folder" width="22" height="18" viewBox="0 0 22 18" fill="none" stroke="#f5c542" stroke-width="1.6"><path d="M1 2h7l2 2h11v13H1z"/><path d="M1 6h20"/></svg>
          <span class="name">Authentication</span><span class="date">03 June 2023</span>
          <svg class="dots" width="6" height="18" viewBox="0 0 6 18" fill="#1d2330"><circle cx="3" cy="3" r="1.8"/><circle cx="3" cy="9" r="1.8"/><circle cx="3" cy="15" r="1.8"/></svg></div>
      </div>

      <div class="abs details">
        <div class="abs section-title" style="left:25px;top:16px">Details</div>
        <svg class="abs" style="left:97px;top:82px" width="87" height="70" viewBox="0 0 87 70"><path d="M0 6a5 5 0 015-5h22l8 8h47a5 5 0 015 5v51a5 5 0 01-5 5H5a5 5 0 01-5-5z" fill="#8ee3ab"/></svg>
        <span class="label" style="top:179px">Category</span>
        <span class="value" style="top:197px">Social Media</span>
        <span class="label" style="top:234px">Owner</span>
        <span class="value" style="top:252px">My Account</span>
        <span class="label" style="top:289px">Last Modified</span>
        <span class="value" style="top:307px">03 June 2023</span>
        <span class="scroll"></span>
      </div>
    </div>
  </section>

</div>
</body>
</html>
```